led light bulb promotional flyer

i need a flyer to help me sell my led light bulbs. I would like a single sided if possible that is if everything fits and looks nice or double sided if not. On the front i would like some details on led bulbs and the benefits they provide over standard incandescent light bulbs. I would like a header to include the pictures attached and my web page www.glowmerchant.ie and my logo

also to include on front page: For the first time ever you can now replace your ordinary incandescent , halogen and CFL bulbs with more energy efficent LED bulbs.

www.glowmerchant.ie can now offer you a complete range of LED bulbs on our website.

FACT: If you have 20 x 50w halogen spotlights in your home they are costing you €720 per year. If you switch to LED bulbs you can save as much as €600 per year which is a saving of 83%
In a domestic setting LED bulbs will pay for themselves within six months too one year depending on usage.

Lightbulbs in pubs , hotels and restaurants are typically switched on for 12 hours per day. At that level of usage energy efficient LED alternatives will pay for themselves in as little as one month. A small investment in LED bulbs will mean great savings in the long run.

Must be stated clearly on the front that delivery is FREE.

Target Market(s)

the target market are home owners in Ireland

Industry/Entity Type

Investment

Requirements
Must have
• on the back of the flyer i want to offer three LED bulbs for sale 3W GU10 LED VORTAN CHIP INSIDE cost €18 Can replace a 35w halogen lamp Lumens 258 warm white Lasts 30 times longer 25 years payes for itself within one year guaranteed for 1yearsaving per year V 35w halogen 92%

6w GU10 LED VORTAN CHIP INSIDE COST €22 Can replace a 50w halogen lamp lumens 320 warm white lasts 30 times longer 25 years Payes for it self within one year guaranteed for 1year Saving per year V 50w halogen 88%

7w LED bulb B22 base KELDO LED INSIDE COST €28 Can replace a 70 w incandecant bulb lumens 530 warm white Last 30 times longer 25 years payes for it self within one year guaranteed for 1 year
saving per year V 70w incandecent 90%
Nice to have
• Irish company.CE logo Rohs logo compliant paysafe verified green - energy saving enviromental save money please take a look at my web page for guidence

```html
<!DOCTYPE html>
<html lang="en">
<head>
<meta charset="utf-8">
<title>Glow Merchant – LED Bulb Flyer</title>
<link rel="stylesheet" href="https://fonts.googleapis.com/css2?family=Cabin:wght@500;600&family=Open+Sans:ital,wght@0,400;0,700;1,700&family=Arimo:ital,wght@0,400;1,400&family=Archivo+Black&display=swap">
<style>
  :root {
    --plum: #2d1a2d;
    --plum-deep: #22121f;
    --sand: #d5c5b6;
    --ink: #2a2a2a;
    --fact-ink: #3a3a3a;
    --white: #ffffff;
    --stripe-dark: #0d0a0c;
  }
  * { margin: 0; padding: 0; box-sizing: border-box; }
  html, body { width: 945px; height: 1200px; overflow: hidden; background: var(--sand); }
  .flyer { position: relative; width: 945px; height: 1200px; background: var(--sand); overflow: hidden; font-family: "Open Sans", sans-serif; }
  .waves { position: absolute; inset: 0; }

  .brand { position: absolute; left: 108px; top: 108px; color: var(--white); }
  .brand-mark { display: flex; align-items: center; gap: 12px; }
  .brand-dot { width: 20px; height: 20px; border-radius: 50%; background: var(--white); }
  .brand-name { font-family: "Arimo", sans-serif; font-size: 50px; font-weight: 400; letter-spacing: -0.5px; line-height: 1; }
  .brand-rule { width: 270px; height: 2px; margin: 10px 0 8px; background: linear-gradient(90deg, rgba(255,255,255,0), #fff 30%, #fff 70%, rgba(255,255,255,0)); }
  .brand-url { font-family: "Arimo", sans-serif; font-size: 27px; }

  .product-photos { position: absolute; left: 443px; top: 56px; width: 412px; height: 252px; border-radius: 18px;
    background: radial-gradient(ellipse at 50% 45%, #bdb7c0 0%, #7f7384 45%, rgba(45,26,45,0) 75%); }

  .headline { position: absolute; left: 60px; width: 825px; top: 418px; text-align: center;
    font-family: "Cabin", sans-serif; font-weight: 600; font-size: 26px; line-height: 32px; color: var(--plum); }

  .promo-band { position: absolute; left: 0; top: 537px; width: 945px; height: 80px; background: var(--plum);
    box-shadow: 0 6px 10px rgba(0,0,0,0.25); color: var(--white); text-align: center;
    font-style: italic; font-weight: 700; font-size: 19.5px; line-height: 28px; padding-top: 12px; }

  .benefits { position: absolute; left: 82px; top: 640px; list-style: none; color: var(--ink); font-size: 18.5px; line-height: 28px; }
  .benefits li { position: relative; padding-left: 40px; margin-bottom: 0; }
  .benefits li::before { content: ""; position: absolute; left: 0; top: 8px; width: 13px; height: 13px; border-radius: 50%;
    background: radial-gradient(circle at 35% 35%, #8d7d93, #3e2c44); }

  .fact { position: absolute; left: 349px; top: 768px; width: 560px; border-left: 1.5px solid var(--plum);
    padding-left: 8px; font-family: "Arimo", sans-serif; font-style: italic; font-size: 14px; line-height: 17px; color: var(--fact-ink); }
  .fact p + p { margin-top: 17px; }

  .delivery-badge { position: absolute; left: 52px; top: 850px; width: 285px; height: 160px; }
  .delivery-text { position: absolute; left: 52px; top: 850px; width: 285px; height: 160px; display: flex; flex-direction: column;
    align-items: center; justify-content: center; transform: rotate(-10deg);
    font-family: "Archivo Black", sans-serif; font-size: 28px; line-height: 32px; color: var(--plum-deep); }

  .contact { position: absolute; left: 0; width: 945px; top: 1066px; text-align: center; color: var(--white);
    font-weight: 700; font-size: 15px; line-height: 25px; }
  .contact-title { font-size: 17px; }
</style>
</head>
<body>
<main class="flyer">
  <svg class="waves" viewBox="0 0 945 1200" width="945" height="1200" aria-hidden="true">
    <path fill="#ffffff" d="M0 0 H945 V488 C905 438 860 388 760 383 C640 378 520 418 380 388 C250 360 150 300 0 263 Z"/>
    <path fill="#2d1a2d" d="M0 0 H945 V470 C905 420 860 370 760 365 C640 360 520 400 380 370 C250 342 150 282 0 245 Z"/>
    <path fill="#0d0a0c" d="M0 868 C120 938 250 968 450 973 C700 978 880 998 945 1052 V1200 H0 Z"/>
    <path fill="#2d1a2d" d="M0 882 C120 952 250 982 450 987 C700 992 880 1012 945 1066 V1200 H0 Z"/>
  </svg>

  <header class="brand">
    <div class="brand-mark">
      <span class="brand-dot"></span>
      <span class="brand-name">Glow Merchant</span>
    </div>
    <div class="brand-rule"></div>
    <div class="brand-url">GlowMerchant.ie</div>
  </header>

  <div class="product-photos" role="img" aria-label="Six LED light bulbs of different shapes: spotlight, globe and corn-style bulbs"></div>

  <h1 class="headline">Are you looking for solutions to reduce your home<br>energy bill. Why not start by replacing your Halogen<br>and incandescent light Bulbs with LED Light Bulbs?</h1>

  <p class="promo-band">For the first time ever you can now replace your ordinary incandescent,<br>halogen and CFL bulbs with more energy efficient LED bulbs.</p>

  <ul class="benefits">
    <li>All our LED bulbs will fit perfectly into your existing fittings.</li>
    <li>Simply replace your halogen or incandescent bulbs with our LED equivalent<br>and save up to 90% on your lighting electricity bill straight away.</li>
    <li>Do it yourself and get immediate savings.</li>
  </ul>

  <div class="fact">
    <p>FACT: If you have 20 x 50w halogen spotlights in your home, they are costing you €720 per year. If you switch to LED bulbs, you can save as much as €600 per year which is a saving of 83%.<br>In a domestic setting, LED bulbs will pay for themselves within six months to one year depending on usage.</p>
    <p>Lightbulbs in pubs, hotels and restaurants are typically switched on for 12 hours per day. At that level of usage energy efficient LED alternatives will pay for themselves in as little as one month. A small investment in LED bulbs will mean great savings in the long run.</p>
  </div>

  <svg class="delivery-badge" viewBox="0 0 285 160" aria-hidden="true">
    <g transform="rotate(-10 142 80)">
      <polygon fill="#2d1a2d" points="142,2 160,16 182,6 194,24 218,20 224,40 250,42 248,62 272,72 258,88 276,104 252,112 256,134 230,134 224,154 200,146 184,162 164,150 142,162 120,150 100,162 84,146 60,154 54,134 28,134 32,112 8,104 26,88 12,72 36,62 34,42 60,40 66,20 90,24 102,6 124,16"/>
      <polygon fill="#ffffff" points="142,14 158,26 178,18 188,34 210,32 214,50 236,52 236,68 256,78 244,90 260,102 240,108 242,126 220,126 214,142 194,136 180,150 162,140 142,150 122,140 104,150 90,136 70,142 64,126 42,126 44,108 24,102 40,90 28,78 48,68 48,52 70,50 74,32 96,34 106,18 126,26"/>
    </g>
  </svg>
  <div class="delivery-text"><span>DELIVERY</span><span>IS FREE</span></div>

  <footer class="contact">
    <div class="contact-title">CONTACT ADDRESS:</div>
    <div>Glow Merchant, Unit 4 Harbour Road, Skerries Co Dublin, Ireland.</div>
    <div>Email: sales@glowmerchant.ie;&nbsp; www.glowmerchant.ie</div>
  </footer>
</main>
</body>
</html>
```